Modern business card design for professional copywriter

I'd like a business card design that I can use to have my cards printed out by plink.com as a squared corners business card (see artwork and design guidelines here: https://help.plink.com/hc/en-gb/sections/300481726-PLINK-Product-Templates)

The design should be clean and modern and reflect the colours, tone and branding on my website: https://noravestrel.com.au

Target Market(s)

Professionals, B2B small business owners

Industry/Entity Type

Business

Contact Information for Business Card

Nora Vestrel
m: 0427 593 864
e: nora@noravestrel.com.au
w: noravestrel.com.au

Font styles to use
Sans Serif

Requirements
Must have
• Tagline: "Smart copywriting for clever business people"
• Brand colours: fd8000, 009984, 666666 and black
Nice to have

```html
<!DOCTYPE html>
<html lang="en">
<head>
<meta charset="utf-8">
<title>Nora Vestrel – Copywriter business card</title>
<link rel="stylesheet" href="https://fonts.googleapis.com/css2?family=Arimo:wght@400&display=swap">
<style>
  :root {
    --brand-green: #3ccf78;
    --brand-orange: #f26a1b;
    --ink-slate: #4a5759;
    --paper: #ffffff;
  }
  * { margin: 0; padding: 0; box-sizing: border-box; }
  html, body { width: 1200px; height: 805px; overflow: hidden; background: var(--paper); }
  .card {
    position: relative;
    width: 1200px;
    height: 805px;
    overflow: hidden;
    background: var(--paper);
    font-family: "Arimo", Arial, sans-serif;
  }
  .card__backdrop {
    position: absolute;
    inset: 0;
    background:
      radial-gradient(ellipse 520px 700px at 0% 75%, rgba(60, 207, 120, 0.55), rgba(60, 207, 120, 0) 70%),
      radial-gradient(ellipse 900px 260px at 70% 108%, rgba(60, 207, 120, 0.5), rgba(60, 207, 120, 0) 70%),
      radial-gradient(ellipse 300px 520px at 100% 10%, rgba(245, 138, 78, 0.55), rgba(245, 138, 78, 0) 70%),
      var(--paper);
  }
  .brand {
    position: absolute;
    left: 318px;
    top: 118px;
  }
  .brand__line {
    display: flex;
    align-items: center;
    gap: 18px;
  }
  .brand__mark {
    width: 70px;
    height: 70px;
    border-radius: 50%;
    background: var(--brand-orange);
    flex: none;
  }
  .brand__name {
    font-size: 92px;
    font-weight: 400;
    line-height: 1;
    color: var(--brand-green);
    white-space: nowrap;
  }
  .brand__role {
    margin: 14px 0 0 88px;
    font-size: 26px;
    letter-spacing: 9px;
    line-height: 1;
    color: var(--ink-slate);
    white-space: nowrap;
  }
  .brand__tagline {
    margin: 12px 0 0 88px;
    font-size: 21px;
    line-height: 1;
    color: var(--ink-slate);
    white-space: nowrap;
  }
  .contact {
    position: absolute;
    left: 0;
    top: 0;
  }
  .contact__name {
    position: absolute;
    left: 432px;
    top: 352px;
    font-size: 54px;
    font-weight: 400;
    line-height: 1;
    color: var(--ink-slate);
    white-space: nowrap;
  }
  .contact__line {
    position: absolute;
    display: flex;
    align-items: center;
    white-space: nowrap;
    color: var(--brand-green);
    line-height: 1;
  }
  .contact__line svg { fill: var(--ink-slate); flex: none; }
  .contact__line--phone { left: 420px; top: 425px; font-size: 47px; gap: 30px; }
  .contact__line--email { left: 456px; top: 490px; font-size: 41px; gap: 32px; }
  .contact__line--web { left: 503px; top: 548px; font-size: 41px; gap: 30px; }
</style>
</head>
<body>
<main class="card">
  <div class="card__backdrop" role="img" aria-label="Soft green and orange flowing ribbon backdrop"></div>

  <header class="brand">
    <div class="brand__line">
      <span class="brand__mark" aria-hidden="true"></span>
      <h1 class="brand__name">Nora Vestrel</h1>
    </div>
    <p class="brand__role">COPYWRITER</p>
    <p class="brand__tagline">Smart copywriting for clever business people</p>
  </header>

  <section class="contact">
    <h2 class="contact__name">Nora Vestrel</h2>
    <p class="contact__line contact__line--phone">
      <svg width="34" height="50" viewBox="0 0 34 50" aria-hidden="true">
        <path d="M6 0 H28 A6 6 0 0 1 34 6 V44 A6 6 0 0 1 28 50 H6 A6 6 0 0 1 0 44 V6 A6 6 0 0 1 6 0 Z M4 7 V38 H30 V7 Z M13 42 V45 H21 V42 Z"/>
      </svg>
      <span>0427 593 864</span>
    </p>
    <p class="contact__line contact__line--email">
      <svg width="52" height="36" viewBox="0 0 52 36" aria-hidden="true">
        <path d="M0 0 H52 L26 20 Z M0 4 L18 18 L0 32 Z M52 4 V32 L34 18 Z M21 20 L26 24 L31 20 L52 36 H0 Z"/>
      </svg>
      <span>nora@noravestrel.com.au</span>
    </p>
    <p class="contact__line contact__line--web">
      <svg width="54" height="54" viewBox="0 0 54 54" aria-hidden="true">
        <path d="M24 2 A22 22 0 1 0 40 41 L37 38 A18 18 0 1 1 42 24 H46 A22 22 0 0 0 24 2 Z"/>
        <path d="M6 16 H42 V19 H6 Z M4 28 H30 V31 H4 Z M22 4 C14 14 14 34 22 44 L19 45 C10 34 10 14 19 3 Z M26 4 C32 10 34 18 34 24 H31 C31 18 29 11 24 5 Z"/>
        <path d="M30 26 L52 36 L43 39 L50 48 L46 51 L39 42 L33 49 Z"/>
      </svg>
      <span>noravestrel.com.au</span>
    </p>
  </section>
</main>
</body>
</html>
```